Design for web app with Plinkora Stratum Craft - Tarvo7 SMS consult

We are developing a web app that will work in browsers. Its main purpose is to allow for users (signing up and logging in with their phone number) to track their habbits and select consultants to whom they can send SMS for help.

The wireframes of the app can be accessed here (pdf):
https://files.plinkora.example/d/7K2mWqLzXv4NtRb9HcJpYsAeUfDg3/view

NB!: Please do not follow the mockups 100% literally, but the Plinkora Stratum craft guidelines.

The technical specifications and descriptions of the web app's functionalities are available in the link below:
https://papers.plinkora.example/doc/4HsTnV8bQeZr2LmXwYcKpDjAuFgN6oRiE5tW1yMx/edit

Requirements for the design:

- The design should be provided as PSD, where each page/section should be in its own PSD file OR all pages/sections should be represented as folder groups in a single PSD file.

- All graphical elements in the design should be delivered as single layers which can then be extracted from the PSD.

- All graphical elements (icons, graphical buttons, etc.) should be provided as vector objects in the PSD, so that they can be exported into different sizes without loss of quality (for responsiveness).

- The design should use either web safe fonts or Plinkora Type.

Instructions for the design:
The design should be based on Plinkora Stratum Craft - http://www.plinkora.example/craft/spec/stratum-craft/overview.html

Please also provide an app icon and suggest a logo for the app.

Requirements
Must have
• Based on Plinkora Stratum Craft
• Flat
Nice to have
• Nice looking and not so stiff as the default Plinkora Stratum Craft, but it is important to follow their guidelines.
Should not have
• 3D

```html
<!DOCTYPE html>
<html lang="en">
<head>
<meta charset="utf-8">
<title>Tarvo7 – Signup</title>
<link rel="stylesheet" href="https://fonts.googleapis.com/css2?family=Open+Sans:wght@300;400;600;700&display=swap">
<style>
  :root {
    --screen-bg: #313131;
    --status-bg: #000000;
    --panel-bg: #0b0b0b;
    --text-light: #ffffff;
    --field-bg: #ffffff;
    --field-text: #1f7bb0;
    --field-divider: #b9b9b9;
    --accent-yellow: #e0bb1e;
    --accent-blue: #044d74;
    --brand-blue: #1d6fa8;
    --dot-idle: #d6d6d6;
    --dot-active: #1b6fa6;
  }
  * { margin: 0; padding: 0; box-sizing: border-box; }
  html, body { width: 676px; height: 1200px; overflow: hidden; background: var(--screen-bg); }
  body { font-family: "Open Sans", Arial, sans-serif; color: var(--text-light); position: relative; }

  .status-bar {
    position: absolute; left: 0; top: 0; width: 676px; height: 63px;
    background: var(--status-bg); display: flex; align-items: center;
    font-weight: 600; font-size: 27px; letter-spacing: 0.5px;
  }
  .status-bar .signal { position: absolute; left: 9px; top: 22px; display: flex; align-items: flex-end; gap: 3px; height: 18px; }
  .status-bar .signal span { display: block; width: 5px; background: #e8e8e8; }
  .status-bar .carrier { position: absolute; left: 56px; top: 12px; }
  .status-bar .clock { position: absolute; left: 0; width: 676px; text-align: center; top: 12px; }
  .status-bar .alarm { position: absolute; left: 587px; top: 20px; }
  .status-bar .battery { position: absolute; left: 624px; top: 19px; }

  .backdrop {
    position: absolute; left: 0; top: 63px; width: 676px; height: 1137px;
    background:
      radial-gradient(ellipse 260px 360px at 500px 560px, rgba(120,100,70,0.55), transparent 70%),
      radial-gradient(ellipse 300px 260px at 520px 1120px, rgba(150,110,70,0.6), transparent 70%),
      linear-gradient(180deg, #333 0%, #353431 40%, #4a4238 100%);
  }

  .app-header { position: absolute; left: 0; top: 63px; width: 676px; height: 150px; }
  .menu-icon { position: absolute; left: 27px; top: 106px; }
  .briefcase-icon { position: absolute; left: 612px; top: 106px; }
  .brand { position: absolute; left: 203px; top: 91px; display: flex; align-items: center; gap: 12px; }
  .brand .mark { width: 30px; height: 30px; background: var(--brand-blue); }
  .brand .name { font-size: 34px; font-weight: 400; color: var(--text-light); letter-spacing: 1px; }

  .signup-panel {
    position: absolute; left: 28px; top: 241px; width: 620px; height: 853px;
    background: var(--panel-bg);
  }
  .signup-panel h1 {
    position: absolute; left: 0; width: 100%; top: 374px; text-align: center;
  }
  .panel-title {
    position: absolute; left: 0; top: 133px; width: 100%; text-align: center;
    font-size: 45px; font-weight: 400; line-height: 1;
  }
  .phone-field {
    position: absolute; left: 79px; top: 248px; width: 464px; height: 60px;
    background: var(--field-bg); border-radius: 5px; display: flex; align-items: center;
  }
  .phone-field .label { padding-left: 28px; font-size: 22px; color: var(--field-text); flex: 1; }
  .phone-field .divider { width: 2px; height: 56px; background: var(--field-divider); }
  .phone-field .icon { width: 58px; display: flex; justify-content: center; }
  .btn {
    position: absolute; left: 79px; width: 464px; height: 60px; border-radius: 5px;
    display: flex; align-items: center; justify-content: center;
    font-size: 29px; font-weight: 700; color: var(--text-light);
    text-shadow: 1px 2px 2px rgba(0,0,0,0.45);
  }
  .btn-signup { top: 353px; background: var(--accent-yellow); }
  .btn-cancel { top: 670px; background: var(--accent-blue); }

  .pager { position: absolute; top: 1142px; left: 306px; display: flex; gap: 9px; }
  .pager span { width: 13px; height: 13px; border-radius: 50%; background: var(--dot-idle); }
  .pager span.active { background: var(--dot-active); }
  .screen-code { position: absolute; left: 619px; top: 1135px; font-size: 15px; color: var(--text-light); }
</style>
</head>
<body>
  <div class="backdrop" role="img" aria-label="Blurred background photo of a person outdoors near water"></div>

  <div class="status-bar">
    <div class="signal"><span style="height:5px"></span><span style="height:8px"></span><span style="height:11px"></span><span style="height:14px"></span><span style="height:18px"></span></div>
    <span class="carrier">LUMA &nbsp;3G</span>
    <span class="clock">4:20 PM</span>
    <svg class="alarm" width="22" height="22" viewBox="0 0 22 22"><circle cx="11" cy="11" r="10" fill="#e8e8e8"/><path d="M11 5v6h4" stroke="#000" stroke-width="2.2" fill="none"/></svg>
    <svg class="battery" width="44" height="24" viewBox="0 0 44 24"><rect x="1" y="2" width="38" height="20" rx="3" fill="none" stroke="#e8e8e8" stroke-width="2"/><rect x="4" y="5" width="32" height="14" rx="1" fill="#e8e8e8"/><rect x="40" y="8" width="3" height="8" fill="#e8e8e8"/></svg>
  </div>

  <header class="app-header">
    <svg class="menu-icon" width="37" height="27" viewBox="0 0 37 27"><rect y="0" width="37" height="6" rx="3" fill="#fff"/><rect y="10.5" width="37" height="6" rx="3" fill="#fff"/><rect y="21" width="37" height="6" rx="3" fill="#fff"/></svg>
    <div class="brand"><span class="mark"></span><span class="name">Tarvo7</span></div>
    <svg class="briefcase-icon" width="36" height="29" viewBox="0 0 36 29"><path d="M12 6V3a2 2 0 0 1 2-2h8a2 2 0 0 1 2 2v3" stroke="#fff" stroke-width="2.5" fill="none"/><rect x="0" y="6" width="36" height="23" rx="3" fill="#fff"/></svg>
  </header>

  <main class="signup-panel">
    <h2 class="panel-title">Signup</h2>
    <div class="phone-field">
      <span class="label">Phone</span>
      <span class="divider"></span>
      <span class="icon">
        <svg width="22" height="26" viewBox="0 0 22 26"><path d="M5 1c1.5-.6 2.5 0 3 1.2l1.5 4c.4 1.1 0 1.9-1 2.5l-1.6 1c.6 2.8 2.3 5.8 4.6 7.6l1.5-1.1c1-.7 1.9-.6 2.6.3l2.6 3.3c.7 1 .6 2-.5 2.9-1.6 1.3-3.4 2-5.2 1.2C6.3 21.5 1.7 14 1.5 7.2 1.5 4.2 2.8 2 5 1z" fill="var(--field-text)"/></svg>
      </span>
    </div>
    <div class="btn btn-signup">Signup</div>
    <div class="btn btn-cancel">Cancel</div>
  </main>

  <nav class="pager" aria-label="Screens"><span></span><span></span><span class="active"></span><span></span><span></span><span></span></nav>
  <span class="screen-code">M3</span>
</body>
</html>
```